German Webagency needs fresh modern Design

Our website is 4 years old. We need an fresh modern website. All pics we used before are from customers or handmade by us. the new website should be clear with nice handling. please dont copy something from template websites. it would be great if you can surprise us with something great. its our first project here. don´t worry if i make a mistake in responding or briefing. after 20 years you can´t see the works of your own "designer" so we hope for help :-)
our existing site: www.tovankreativ.de
Target Market(s)
small and middle sized companys in germany
Number of Pages Required
4 page
Font styles to use
Colors
Designer to choose colors to be used in the design.
Requirements
Must have
- Responsive (sure we code it)
- Modern and big Font ..Headlines and Slider
- innovative..if you know something new..feel free to show
Nice to have
- the site with our works/refences should look great and later easy to handle when we code it or use wp.
- we like black and grey but if you have better ideas also feel free
Should not have
- a cup of coffe..laptop.. a pencil a handwritten font
- dont copy and modify templates from know websites..bad style

```html
<!DOCTYPE html>
<html lang="de">
<head>
<meta charset="utf-8">
<title>tovankreativ.de – Webagentur</title>
<link href="https://fonts.googleapis.com/css2?family=Montserrat:wght@400;500;600;700&family=Open+Sans:wght@400;600&display=swap" rel="stylesheet">
<style>
:root{
  --blue:#3a85d4;
  --blue-dark:#2f6fb6;
  --red:#e2383f;
  --ink:#24272c;
  --tile:#272b31;
  --footer:#1e2126;
  --grey-bg:#eeeff1;
  --text:#6b7079;
  --white:#ffffff;
}
*{box-sizing:border-box;margin:0;padding:0}
html,body{width:1200px;height:2980px;overflow:hidden}
body{font-family:"Open Sans",Arial,sans-serif;color:var(--ink);background:var(--white)}
h1,h2,h3,.nav,.btn,.tab,.tile{font-family:"Montserrat",Arial,sans-serif}

.site-header{height:72px;display:flex;align-items:center;justify-content:space-between;padding:0 172px;background:var(--white)}
.logo{display:flex;align-items:center;gap:10px;font-family:"Montserrat",Arial,sans-serif;font-weight:700;font-size:22px;color:var(--ink)}
.logo-dot{width:14px;height:14px;border-radius:50%;background:var(--blue)}
.nav{display:flex;align-items:center;gap:26px;font-size:12px;font-weight:600;color:var(--ink);letter-spacing:.5px}
.nav .btn-contact{background:var(--blue);color:var(--white);padding:10px 26px;border-radius:2px}

.hero{position:relative;height:508px;background:linear-gradient(180deg,#5c6f86 0%,#8da2b6 35%,#4f5d52 70%,#37413f 100%);color:var(--white)}
.hero-title{position:absolute;left:172px;top:28px}
.hero-title h1{font-size:38px;font-weight:700;letter-spacing:1px}
.hero-title p{font-size:15px;margin-top:8px}
.hero-arrow{position:absolute;top:300px;width:30px;height:40px}
.hero-arrow.left{left:140px}.hero-arrow.right{right:140px}

.services{height:592px;text-align:center;padding-top:68px}
.section-title{font-size:42px;font-weight:500;letter-spacing:1px;color:var(--ink)}
.section-intro{width:560px;margin:14px auto 0;font-size:13px;line-height:20px;color:var(--text)}
.tile-grid{display:grid;grid-template-columns:repeat(4,196px);gap:20px 22px;justify-content:center;margin-top:40px}
.tile{height:144px;background:var(--tile);color:var(--white);display:flex;flex-direction:column;align-items:center;justify-content:center;gap:12px;font-size:12px;font-weight:600;text-transform:uppercase;padding:0 20px;line-height:17px}
.tile.active{background:var(--blue)}
.tile svg{width:36px;height:36px}

.tabs{display:flex;height:100px}
.tab{flex:1;display:flex;align-items:center;justify-content:center;gap:12px;color:var(--white);font-size:20px;font-weight:500}
.tab.overview{background:var(--blue)}.tab.team{background:var(--red)}.tab.careers{background:var(--blue-dark)}

.feature{height:428px;background:linear-gradient(180deg,#2b2622 0%,#3d342c 50%,#221e1b 100%);color:var(--white);text-align:center;padding-top:86px}
.feature h2{font-size:40px;font-weight:700;letter-spacing:1px}
.feature .play{margin:18px auto 0;width:40px;height:40px}
.feature p{width:640px;margin:22px auto 0;font-size:14px;line-height:22px}
.btn-outline{display:inline-block;margin-top:30px;border:2px solid var(--white);padding:10px 26px;font-size:12px;font-weight:600;letter-spacing:1px}

.franchise{height:240px;background:var(--blue);color:var(--white);padding:62px 172px 0}
.franchise h2{font-size:32px;font-weight:700}
.franchise p{width:720px;margin-top:14px;font-size:14px;line-height:22px}
.franchise .arrow{margin-top:18px;width:30px;height:14px}

.blog{height:508px;text-align:center;padding-top:62px}
.card-row{display:flex;justify-content:center;gap:24px;margin-top:34px}
.card{width:272px;text-align:left;background:var(--white);box-shadow:0 2px 8px rgba(0,0,0,.12)}
.card-image{height:144px}
.card-body{padding:18px 20px 22px}
.card h3{font-size:16px;font-weight:600;color:var(--blue);line-height:22px}
.card p{font-size:12px;line-height:18px;color:var(--text);margin-top:10px}
.card .more{margin-top:14px;width:22px;height:10px}

.cta{position:relative;height:352px;background:var(--grey-bg);text-align:center;padding-top:66px}
.cta h2{font-size:38px;font-weight:700;letter-spacing:1px}
.cta p{width:560px;margin:14px auto 0;font-size:13px;line-height:20px;color:var(--text)}
.btn-solid{display:inline-block;margin-top:22px;background:var(--blue);color:var(--white);padding:13px 34px;font-size:12px;font-weight:600;letter-spacing:1px}
.skyline{position:absolute;left:0;right:0;bottom:0;height:140px;background:linear-gradient(180deg,rgba(30,33,38,0) 0%,var(--footer) 70%)}

.site-footer{height:180px;background:var(--footer);color:#9aa0a8;padding:34px 172px 0;font-size:12px}
.footer-top{display:flex;align-items:center;justify-content:space-between}
.footer-top .logo{color:var(--white);font-size:20px}
.social{display:flex;gap:12px}
.social span{width:14px;height:14px;border-radius:50%;background:#5a6068}
.footer-bottom{display:flex;justify-content:space-between;margin-top:34px;border-top:1px solid #33373d;padding-top:20px}
.footer-nav{display:flex;gap:22px;font-family:"Montserrat",Arial,sans-serif;font-weight:600;font-size:11px;color:#c4c8cd}
</style>
</head>
<body>

<header class="site-header">
  <div class="logo"><span class="logo-dot"></span>tovankreativ.de</div>
  <nav class="nav">
    <span>HOME</span><span>ZIELE</span><span>ÜBER UNS</span><span>SERVICES</span><span>REFERENZEN</span><span>AKTUELLES</span><span class="btn-contact">KONTAKT</span>
  </nav>
</header>

<section class="hero" role="img" aria-label="Stadtpanorama mit Hochhäusern und Fluss unter bewölktem Himmel">
  <div class="hero-title">
    <h1>IDEEN &amp; VISIONEN GEMEINSAM VERWIRKLICHEN !</h1>
    <p>Neue Website • Mehr Umsatz • Neue Kunden</p>
  </div>
  <svg class="hero-arrow left" viewBox="0 0 30 40"><path d="M22 4 8 20l14 16" fill="none" stroke="#fff" stroke-width="4"/></svg>
  <svg class="hero-arrow right" viewBox="0 0 30 40"><path d="M8 4l14 16L8 36" fill="none" stroke="#fff" stroke-width="4"/></svg>
</section>

<section class="services">
  <h2 class="section-title">OUR SERVICES</h2>
  <p class="section-intro">We plan, design and build digital work for small and mid-sized companies. Clear structure, strong visuals and measurable results for every project.</p>
  <div class="tile-grid">
    <div class="tile active"><svg viewBox="0 0 36 36"><circle cx="18" cy="18" r="14" fill="none" stroke="#fff" stroke-width="2"/><path d="M18 8v10l7 5" fill="none" stroke="#fff" stroke-width="2"/></svg>Strategy &amp; Consulting</div>
    <div class="tile">Content Marketing</div>
    <div class="tile">Website Design and Development</div>
    <div class="tile">Video Production</div>
    <div class="tile">SEO, PPC &amp; Online Marketing</div>
    <div class="tile">Social Media &amp; Reputation Management</div>
    <div class="tile">Location Marketing</div>
    <div class="tile">View More Project</div>
  </div>
</section>

<div class="tabs">
  <div class="tab overview"><svg width="20" height="14" viewBox="0 0 20 14"><ellipse cx="10" cy="7" rx="9" ry="6" fill="none" stroke="#fff" stroke-width="1.6"/><circle cx="10" cy="7" r="2.5" fill="#fff"/></svg>Overview</div>
  <div class="tab team"><svg width="16" height="16" viewBox="0 0 16 16"><circle cx="8" cy="5" r="3.5" fill="none" stroke="#fff" stroke-width="1.6"/><path d="M1 16c0-4 3-6 7-6s7 2 7 6" fill="none" stroke="#fff" stroke-width="1.6"/></svg>Team</div>
  <div class="tab careers"><svg width="18" height="16" viewBox="0 0 18 16"><rect x="1" y="4" width="16" height="11" fill="none" stroke="#fff" stroke-width="1.6"/><path d="M6 4V1h6v3" fill="none" stroke="#fff" stroke-width="1.6"/></svg>Careers</div>
</div>

<section class="feature" role="img" aria-label="Dunkles Foto eines Arbeitsraums als Hintergrund">
  <h2>WEBDESIGN &amp; GRAFIKDESIGN</h2>
  <svg class="play" viewBox="0 0 40 40"><circle cx="20" cy="20" r="18" fill="none" stroke="#fff" stroke-width="2"/><path d="M16 12l12 8-12 8z" fill="#fff"/></svg>
  <p>We create websites and brand design that bring your company to the screen with clarity. From first sketch to launch, every detail is planned for your customers and your goals.</p>
  <span class="btn-outline">LEARN MORE</span>
</section>

<section class="franchise">
  <h2>FRANCHISE MARKETING AND DEVELOPMENT</h2>
  <p>Integrated strategies that bring search, social, local and mobile together for franchise brands, local businesses and growing teams.</p>
  <svg class="arrow" viewBox="0 0 30 14"><path d="M0 7h26M20 1l7 6-7 6" fill="none" stroke="#fff" stroke-width="2"/></svg>
</section>

<section class="blog">
  <h2 class="section-title">RECENT BLOG POSTS</h2>
  <div class="card-row">
    <article class="card">
      <div class="card-image" role="img" aria-label="Foto zum Thema Social Media" style="background:linear-gradient(135deg,#5d8fc4,#c9d6e2)"></div>
      <div class="card-body"><h3>5 Ways to Improve Your Social Content Marketing</h3><p>Simple steps to plan posts your audience actually wants to read.</p><svg class="more" viewBox="0 0 22 10"><path d="M0 5h19M14 1l5 4-5 4" fill="none" stroke="#6b7079" stroke-width="1.6"/></svg></div>
    </article>
    <article class="card">
      <div class="card-image" role="img" aria-label="Foto zum Thema Franchise-Entwicklung" style="background:linear-gradient(135deg,#b8c0c8,#eef0f2)"></div>
      <div class="card-body"><h3>Franchise Development Marketing Tips</h3><p>What new franchise partners should know before the first campaign starts.</p><svg class="more" viewBox="0 0 22 10"><path d="M0 5h19M14 1l5 4-5 4" fill="none" stroke="#6b7079" stroke-width="1.6"/></svg></div>
    </article>
    <article class="card">
      <div class="card-image" role="img" aria-label="Foto zum Thema lokales Marketing" style="background:linear-gradient(135deg,#3f4a57,#8b9aa8)"></div>
      <div class="card-body"><h3>Local Inbound Marketing in 3 Quick Steps</h3><p>Get found nearby with clear listings, reviews and useful local content.</p><svg class="more" viewBox="0 0 22 10"><path d="M0 5h19M14 1l5 4-5 4" fill="none" stroke="#6b7079" stroke-width="1.6"/></svg></div>
    </article>
  </div>
</section>

<section class="cta">
  <h2>LEARN HOW WE CAN HELP YOU</h2>
  <p>Tell us about your company and your goals. We will show you clear next steps for your website.</p>
  <span class="btn-solid">REQUEST A FREE CONSULT</span>
  <div class="skyline" role="img" aria-label="Silhouette einer Stadtsilhouette"></div>
</section>

<footer class="site-footer">
  <div class="footer-top">
    <div class="logo"><span class="logo-dot"></span>tovankreativ.de</div>
    <span>Musterstraße 12, 80331 München</span>
    <span>+49 89 1234 567</span>
    <div class="social"><span></span><span></span><span></span><span></span><span></span></div>
  </div>
  <div class="footer-bottom">
    <div class="footer-nav"><span>HOME</span><span>ZIELE</span><span>ÜBER UNS</span><span>SERVICES</span><span>REFERENZEN</span><span>AKTUELLES</span><span>KONTAKT</span></div>
    <span>© 2024 www.tovankreativ.de. Alle Rechte vorbehalten.</span>
  </div>
</footer>

</body>
</html>
```